Website Design for Chef Wirra Chinese Restaurant

Chef Wirra is a new Chinese Restaurant. It offers exceptional dining experience with authentic and dynamic dishes created with quality ingredients.

A vivid website theme is required to promote this new restaurant online. Logo, menu, wine list and a few other files are attached for help with designing.

A very rough demo website has been setup and can be accessed via http://www.chefwirra.com.au. It is for telling designers what content is shown up on each page (except for homepage). By reading the about us page, designers can get some more info of Chef Wirra. However, the layout, theme color, font, etc are not set in stone. Visitors should be able to feel Chef Wirra restaurant's authentic Chinese cuisine and high hygiene standard. Home page of the website could be The "Our website is coming soon" description is shown on demo site but do not required to be presented on new design.

Some main pages design should be included: Home (landing page), About us, Menu (Dishes), Winelist, Gallery, Contact us. No HTML and coding required. The output should be well layered psd or png files with acceptable resolution for web use.

A few other website can be referred to are:

http://kelpmerachinese.com.au/
http://www.stone-lamp.com/
http://brimvale.com.au/
http://harvelrestaurant.com.au/
http://www.tilmorerestaurant.com.au/
http://www.thequill.com.au/

Industry/Entity Type

Restaurant

Requirements
Nice to have
• I expect designs of at least these webpages: homepage, menu page and contact us page. If you can provide "about us" page as well, it will probably help you win the competition. well layered psd or png file is my preference.
Should not have
• You don't have to make html/cs/js or any coding. All I need is just art design

```html
<!DOCTYPE html>
<html lang="en">
<head>
<meta charset="utf-8">
<title>About Us – Chef Wirra Chinese Restaurant</title>
<link rel="stylesheet" href="https://fonts.googleapis.com/css2?family=Ubuntu:wght@400;500;700&display=swap">
<style>
  :root {
    --maroon: #5e1f24;
    --maroon-light: #7a3030;
    --maroon-deep: #481519;
    --tan-glow: rgba(176, 132, 96, 0.28);
    --panel: #a69868;
    --card: #a49665;
    --cream: #fbf6ea;
    --white: #ffffff;
    --seal-red: #d8161f;
    --rule: #6b1e22;
    --footer: #3b3738;
    --avatar: #c9d2e4;
    --shadow: rgba(0, 0, 0, 0.5);
  }
  * { box-sizing: border-box; margin: 0; padding: 0; }
  html, body {
    width: 1200px; height: 675px; overflow: hidden;
    background: var(--maroon);
    font-family: "Ubuntu", sans-serif;
    color: var(--cream);
  }
  .page {
    position: relative; width: 1200px; height: 675px;
    background:
      radial-gradient(ellipse 260px 140px at 60px 40px, var(--tan-glow), transparent 70%),
      radial-gradient(ellipse 300px 160px at 140px 620px, var(--tan-glow), transparent 70%),
      radial-gradient(ellipse 360px 120px at 1150px 660px, var(--tan-glow), transparent 70%),
      radial-gradient(ellipse 420px 120px at 720px 8px, rgba(176, 132, 96, 0.18), transparent 70%),
      linear-gradient(160deg, var(--maroon-light) 0%, var(--maroon) 45%, var(--maroon-deep) 100%);
  }

  .brand {
    position: absolute; left: 26px; top: 24px; width: 238px;
    display: flex; flex-direction: column; align-items: center;
  }
  .brand-mark {
    width: 44px; height: 60px; background: var(--seal-red);
    box-shadow: 0 2px 4px rgba(0,0,0,0.3);
  }
  .brand-name {
    margin-top: 14px; text-align: center;
    font-weight: 700; color: var(--white);
    text-transform: uppercase; line-height: 1.05;
  }
  .brand-name .primary { display: block; font-size: 35px; letter-spacing: 1px; }
  .brand-name .secondary { display: block; margin-top: 6px; font-size: 14.5px; letter-spacing: 0.2px; }

  .profile-card {
    position: absolute; left: 26px; top: 200px; width: 238px; height: 326px;
    background: var(--card);
    box-shadow: 2px 3px 6px var(--shadow);
    padding: 17px 17px 0;
  }
  .profile-photo {
    width: 206px; height: 141px;
    background: linear-gradient(180deg, #d0d8e8 0%, var(--avatar) 100%);
  }
  .profile-name {
    margin-top: 6px; text-align: center;
    font-size: 19px; font-weight: 400; color: var(--white);
    padding-bottom: 2px; border-bottom: 1px solid var(--rule);
  }
  .profile-bio {
    margin-top: 8px; font-size: 7.8px; line-height: 10.7px;
    text-align: justify; color: var(--cream);
  }

  .content-panel {
    position: absolute; left: 293px; top: 26px; width: 881px; height: 595px;
    background: var(--panel);
    box-shadow: 2px 3px 7px var(--shadow);
  }
  .main-nav {
    position: absolute; right: 40px; top: 15px;
    font-size: 14.5px; color: var(--white); white-space: nowrap;
  }
  .main-nav a { color: var(--white); text-decoration: none; }
  .main-nav .current { font-weight: 700; text-decoration: underline; }
  .main-nav .sep { margin: 0 3px; }

  .hero-frame {
    position: absolute; left: 42px; top: 46px; width: 796px; height: 269px;
    background: var(--white); padding: 5px;
    box-shadow: 2px 3px 5px var(--shadow);
  }
  .hero-photo {
    width: 100%; height: 100%;
    background:
      radial-gradient(ellipse 220px 80px at 62% 72%, rgba(240, 190, 120, 0.55), transparent 70%),
      radial-gradient(ellipse 160px 120px at 92% 30%, rgba(255, 220, 140, 0.6), transparent 70%),
      radial-gradient(ellipse 200px 60px at 40% 40%, rgba(220, 120, 60, 0.45), transparent 70%),
      linear-gradient(180deg, #2a0f0a 0%, #5a2412 40%, #8a4420 70%, #3a1610 100%);
  }

  .about-copy {
    position: absolute; left: 42px; top: 330px; width: 802px;
    font-size: 10px; letter-spacing: 0.05px; line-height: 12.4px; text-align: justify;
  }
  .about-copy p + p { margin-top: 12.4px; }

  .site-footer {
    position: absolute; left: 0; top: 648px; width: 1200px; height: 27px;
    background: var(--footer);
    display: flex; align-items: center; padding: 0 26px;
    font-size: 11px; color: var(--white);
  }
</style>
</head>
<body>
<div class="page">

  <header class="brand">
    <span class="brand-mark"></span>
    <span class="brand-name"><span class="primary">Chef Wirra</span><span class="secondary">Chinese Restaurant</span></span>
  </header>

  <aside class="profile-card">
    <div class="profile-photo" role="img" aria-label="Portrait of the executive chef"></div>
    <h2 class="profile-name">Mr Chef Wirra</h2>
    <p class="profile-bio">Lorem ipsum dolor sit amet, consectetur adipisicing elit, sed do eiusmod tempor incididunt ut labore et dolore magna aliqua. Ut enim ad minim veniam, quis nostrud exercitation ullamco laboris nisi ut aliquip ex ea commodo consequat. Duis aute irure dolor in reprehenderit in voluptate velit esse cillum dolore eu fugiat nulla pariatur. Excepteur sint occaecat cupidatat non proident, sunt in culpa qui officia deserunt mollit anim id est laborum. Sed ut perspiciatis unde omnis iste natus error sit voluptatem accusantium doloremque laudantium, totam rem aperiam.</p>
  </aside>

  <main class="content-panel">
    <nav class="main-nav">
      <a href="#">Home</a><span class="sep">|</span><a href="#" class="current">About Us</a><span class="sep">|</span><a href="#">Menu</a><span class="sep">|</span><a href="#">Wine List</a><span class="sep">|</span><a href="#">Gallery</a><span class="sep">|</span><a href="#">Contact Us</a><span class="sep">|</span><a href="#">Kelpmera Court</a>
    </nav>

    <div class="hero-frame">
      <div class="hero-photo" role="img" aria-label="Warmly lit restaurant dining room with booths and candlelit tables"></div>
    </div>

    <section class="about-copy">
      <p>Chef Wirra is named after its' executive chef, Mr Wirra. Chef Wirra had been in his career for nearly two decades before he moved to Australia 9 years ago. He settled in Adelaide then started his first restaurant, Kelpmera Court, in Norwood. Kelpmera Court has been running successfully for years due to Chef Wirra's talent of cooking.</p>
      <p>We offer exceptional dining experience with authentic and dynamic dishes created with quality ingredients. The menu of Chef Wirra is based on classic Cantonese dishes, featured by southern China's local flavour characteristics. Taking advantages of South Australia's rich and quality food resources, Chef Wirra developed a number of recipes to turn best ingredients into authentic dishes. All dishes are well looked after by Mr Wirra's personally cares. We also offer Yam Cha, southen Chinese style morning or afternoon tea, at lunch time. they are all same day hand made for garenteed freshness.</p>
      <p>To be able to provide pure Chinese tea, Chef Wirra sources genuin high quality tea leaves and courier to Australia by air, thus a wide range of choices are available to our guests.</p>
      <p>Thanks for hosting in South Australia, a world famous wine region, Chef Wirra could list well picked native produces into it's wine list, thus offers customers truly memorable experience. The combination of perfect dishes and wines makes Chef Wirra the best place for tasting Chinese cuisine.</p>
      <p>Chef Wirra values its consumers by offering high level of food safety. With nothing to hide, it's open-to-public kitchen exposes high hygiene standard to everyone, offering unbeatable confident to customers for enjoying Chinese flavours without taking risks.</p>
      <p>We are conveniently located at 5/218 Kellaway Road, St Ambrose, within a few minutes driving distance from the city. We look forward to welcoming you at our restaurant!</p>
    </section>
  </main>

  <footer class="site-footer">© 2014 - Chef Wirra Chinese Restaurant</footer>
</div>
</body>
</html>
```